"Oral Surgery Office needs a Business Card Design with Logo"

We need a logo design and business card. The name of the office is Tassingford Oral Surgery & Implant Center. The final design should communicate uniqueness as well as highly class office. The business card should emphasize power. I included the current business card below. Please design something unique

Target Market(s)

Dentists & Patients

Industry/Entity Type

Dental

Contact Information for Business Card

Unique Design to show success, prestige, Style, unmatched performance

Font styles to use
Serif

Colors
1b1b1b
ffffff
0556a4

Requirements
Must have
• Bussiness Name, Doctor's Name, Website, phone and Fax, email, office address
• Color should be either Black and White or Blue and White
Nice to have
• Clean look
Should not have
• the business card shouldn't be too busy. I feel like the old business card was too busy

```html
<!DOCTYPE html>
<html lang="en">
<head>
<meta charset="utf-8">
<title>Tassingford Oral Surgery &amp; Implant Center – Business Card</title>
<link rel="stylesheet" href="https://fonts.googleapis.com/css2?family=Open+Sans:wght@400;600;700&display=swap">
<style>
  :root {
    --navy: #1c4585;
    --teal: #1a86b5;
    --steel: #7e9fc9;
    --white: #ffffff;
    --ink: #3a3a3a;
    --backdrop: #ececec;
  }
  * { box-sizing: border-box; margin: 0; padding: 0; }
  html, body { width: 1108px; height: 1200px; overflow: hidden; }
  body {
    background: var(--backdrop);
    font-family: "Open Sans", Arial, sans-serif;
    position: relative;
  }
  .card {
    position: absolute;
    left: 122px;
    width: 840px;
    overflow: hidden;
    box-shadow: 0 2px 6px rgba(0,0,0,0.18);
  }
  .card-front { top: 74px; height: 499px; background: var(--navy); }
  .card-back { top: 637px; height: 496px; background: var(--white); }
  .stripe { position: absolute; left: 0; width: 100%; height: 18px; display: block; }
  .front-stripe-top { top: 31px; }
  .front-stripe-bottom { bottom: 28px; }
  .back-stripe { bottom: 27px; }

  .front-mark {
    position: absolute;
    left: 347px; top: 91px;
    width: 156px; height: 156px;
    border: 5px solid var(--white);
    border-radius: 50%;
  }
  .front-name {
    position: absolute;
    left: 0; width: 100%;
    text-align: center;
    color: var(--white);
    font-weight: 600;
  }
  .front-name-primary { top: 296px; font-size: 27px; letter-spacing: 9px; }
  .front-name-secondary { top: 356px; font-size: 31px; letter-spacing: 0.5px; }

  .back-mark {
    position: absolute;
    left: 53px; top: 31px;
    width: 88px; height: 88px;
    border: 4px solid var(--navy);
    border-radius: 50%;
  }
  .back-name {
    position: absolute;
    left: 152px; top: 42px;
    color: var(--navy);
    font-weight: 600;
    line-height: 24px;
    font-size: 18px;
  }
  .back-name-primary { letter-spacing: 5px; }
  .doctor {
    position: absolute;
    left: 58px; top: 162px;
  }
  .doctor-name { color: var(--navy); font-weight: 700; font-size: 25px; line-height: 32px; }
  .doctor-title { color: var(--ink); font-size: 22px; line-height: 30px; }
  .contact-list {
    position: absolute;
    left: 124px; top: 242px;
    list-style: none;
    color: var(--ink);
    font-size: 22px;
  }
  .contact-list li { display: flex; align-items: center; height: 32px; }
  .contact-list li.web { margin-top: 11px; }
  .contact-icon { width: 22px; height: 22px; margin-right: 4px; fill: var(--navy); flex: none; }
</style>
</head>
<body>

<section class="card card-front" aria-label="Business card front">
  <svg class="stripe front-stripe-top" viewBox="0 0 840 18" preserveAspectRatio="none">
    <rect width="840" height="18" fill="var(--teal)"/>
    <polygon points="425,18 448,0 840,0 840,18" fill="var(--steel)"/>
  </svg>
  <div class="front-mark"></div>
  <p class="front-name front-name-primary">TASSINGFORD</p>
  <p class="front-name front-name-secondary">ORAL SURGERY &amp; IMPLANT CENTER</p>
  <svg class="stripe front-stripe-bottom" viewBox="0 0 840 18" preserveAspectRatio="none">
    <rect width="840" height="18" fill="var(--teal)"/>
    <polygon points="0,0 420,0 397,18 0,18" fill="var(--steel)"/>
  </svg>
</section>

<section class="card card-back" aria-label="Business card back">
  <div class="back-mark"></div>
  <div class="back-name">
    <p class="back-name-primary">TASSINGFORD</p>
    <p>ORAL SURGERY</p>
    <p>&amp; IMPLANT CENTER</p>
  </div>

  <div class="doctor">
    <p class="doctor-name">DR. Marcus Ellery, D.D.S.</p>
    <p class="doctor-title">Oral and Maxillofacial Surgery</p>
  </div>

  <ul class="contact-list">
    <li>
      <svg class="contact-icon" viewBox="0 0 24 24"><path d="M12 3 2 11h3v9h5v-6h4v6h5v-9h3z"/></svg>
      2840 Harbor Lane, Tassingford, NY 11990
    </li>
    <li>
      <svg class="contact-icon" viewBox="0 0 24 24"><path d="M6.6 10.8a15 15 0 0 0 6.6 6.6l2.2-2.2a1 1 0 0 1 1-.25 11.4 11.4 0 0 0 3.6.57 1 1 0 0 1 1 1V20a1 1 0 0 1-1 1A17 17 0 0 1 3 4a1 1 0 0 1 1-1h3.5a1 1 0 0 1 1 1c0 1.25.2 2.45.57 3.57a1 1 0 0 1-.25 1z"/></svg>
      555-201-4700
    </li>
    <li>
      <svg class="contact-icon" viewBox="0 0 24 24"><path d="M7 3h8l3 3v4H7zM4 11h16a2 2 0 0 1 2 2v6H2v-6a2 2 0 0 1 2-2zm3 4v2h2v-2zm4 0v2h2v-2zm4 0v2h2v-2z"/></svg>
      555-201-5006
    </li>
    <li>
      <svg class="contact-icon" viewBox="0 0 24 24"><path d="M2 6h20v12H2zm2 2v.5l8 5 8-5V8l-8 5z"/></svg>
      TassingfordOralSurgery.com
    </li>
    <li class="web">
      <svg class="contact-icon" viewBox="0 0 24 24"><circle cx="12" cy="12" r="9" fill="none" stroke="var(--navy)" stroke-width="2"/><path d="M3 12h18M12 3c3 3 3 15 0 18M12 3c-3 3-3 15 0 18" fill="none" stroke="var(--navy)" stroke-width="1.6"/></svg>
      www.TassingfordOralSurgery.com
    </li>
  </ul>

  <svg class="stripe back-stripe" viewBox="0 0 840 18" preserveAspectRatio="none">
    <rect width="840" height="18" fill="var(--teal)"/>
    <polygon points="0,0 422,0 404,18 0,18" fill="var(--navy)"/>
  </svg>
</section>

</body>
</html>
```